Business card for massage therapy company called Brook Fern Wellness

Need business card for massage therapy company called Brook Fern Wellness. Would like my logo on the front and the back of the card I have 3 options of logos and you can play with what looks better.

Would like this information displayed on the back of the card:

Marcus Ellery
Licensed Massage Therapist
321-555-0147
brookfern-example.com
brookfern_rest_

```html
<!DOCTYPE html>
<html lang="en">
<head>
<meta charset="utf-8">
<title>Brook Fern Wellness — Business Card</title>
<link rel="stylesheet" href="https://fonts.googleapis.com/css2?family=Cinzel:wght@400;500&family=Josefin+Sans:wght@300;400&display=swap">
<style>
  :root {
    --sage: #7bcdab;
    --sage-light: #a6dcc5;
    --paper: #ffffff;
    --gap: #ffffff;
  }
  html, body {
    margin: 0;
    padding: 0;
    width: 1016px;
    height: 1200px;
    overflow: hidden;
    background: var(--gap);
  }
  .canvas {
    position: relative;
    width: 1016px;
    height: 1200px;
  }
  .card {
    position: absolute;
    left: 0;
    width: 1016px;
    overflow: hidden;
  }
  .card--front {
    top: 0;
    height: 590px;
    background: var(--paper);
  }
  .card--back {
    top: 598px;
    height: 590px;
    background: var(--sage);
  }
  .wave {
    position: absolute;
    left: 0;
    top: 0;
    width: 1016px;
    height: 590px;
  }
  .brand-seal {
    position: absolute;
    left: 55px;
    top: 110px;
    width: 250px;
    height: 250px;
    border: 3px solid var(--sage);
    border-radius: 50%;
    box-sizing: border-box;
    display: flex;
    align-items: center;
    justify-content: center;
    text-align: center;
    font-family: "Josefin Sans", sans-serif;
    font-weight: 400;
    font-size: 24px;
    line-height: 1.25;
    letter-spacing: 3px;
    color: var(--sage);
    text-transform: uppercase;
  }
  .therapist {
    position: absolute;
    left: 356px;
    top: 180px;
    color: var(--sage);
    font-family: "Cinzel", serif;
  }
  .therapist__name {
    margin: 0;
    font-weight: 500;
    font-size: 68px;
    line-height: 1;
    letter-spacing: 1px;
  }
  .therapist__title {
    margin: 8px 0 0 42px;
    font-weight: 400;
    font-size: 25px;
    letter-spacing: 2.5px;
  }
  .contact-line {
    position: absolute;
    left: 26px;
    top: 532px;
    margin: 0;
    font-family: "Cinzel", serif;
    font-weight: 500;
    font-size: 26px;
    letter-spacing: 0.5px;
    color: var(--paper);
    white-space: nowrap;
    word-spacing: 2px;
  }
  .back-seal {
    position: absolute;
    left: 370px;
    top: 70px;
    width: 274px;
    height: 274px;
    border: 3px solid var(--paper);
    border-radius: 50%;
    box-sizing: border-box;
  }
  .wordmark {
    position: absolute;
    left: 0;
    top: 362px;
    width: 1016px;
    text-align: center;
    color: var(--paper);
    font-family: "Josefin Sans", sans-serif;
  }
  .wordmark__name {
    margin: 0;
    font-weight: 300;
    font-size: 92px;
    line-height: 1;
    letter-spacing: 4px;
  }
  .wordmark__tag {
    margin: 20px 0 0 10px;
    font-weight: 400;
    font-size: 44px;
    letter-spacing: 12px;
  }
</style>
</head>
<body>
<main class="canvas">

  <section class="card card--front" aria-label="Card front">
    <svg class="wave" viewBox="0 0 1016 590" aria-hidden="true">
      <path d="M0 484 C180 468 360 478 540 506 C720 530 880 500 1016 456 L1016 590 L0 590 Z" fill="var(--sage-light)"/>
      <path d="M0 494 C180 478 360 488 540 516 C720 540 880 510 1016 466 L1016 590 L0 590 Z" fill="var(--sage)"/>
    </svg>

    <div class="brand-seal">Brook<br>Fern<br>Wellness</div>

    <div class="therapist">
      <h1 class="therapist__name">Marcus Ellery</h1>
      <p class="therapist__title">Licensed Massage Therapist</p>
    </div>

    <p class="contact-line">321-555-0147 brookfern-example.com brookfern_rest_</p>
  </section>

  <section class="card card--back" aria-label="Card back">
    <div class="back-seal"></div>
    <div class="wordmark">
      <h2 class="wordmark__name">BROOK FERN</h2>
      <p class="wordmark__tag">WELLNESS</p>
    </div>
  </section>

</main>
</body>
</html>
```